Need Business Card ASAP

We need a business card design for a meeting coming up in a few days. The company name is Halvorne Building and Construction and the logo is attached. Something clean, cool, and contemporary that we can get to a printer right away. Attached is the business card for Murrow Energy, an affiliated company, which we like. Instead of the hawk on the back, you could use the attached "D". We'll also be needing matching letterhead in the near future, so ideas for that are welcome.

```html
<!DOCTYPE html>
<html lang="en">
<head>
<meta charset="utf-8">
<title>Halvorne Building &amp; Construction – Business Card</title>
<link rel="stylesheet" href="https://fonts.googleapis.com/css2?family=Cabin:wght@400;600;700&display=swap">
<style>
  :root {
    --sheet: #ffffff;
    --olive: #b3a86a;
    --olive-light: #c2b87e;
    --olive-dark: #a39758;
    --ink: #1f1c1d;
    --band: #231f20;
    --cream: #f4f0e0;
    --white: #ffffff;
    --crop: #9a9a9a;
  }
  * { box-sizing: border-box; margin: 0; padding: 0; }
  html, body {
    width: 900px; height: 1200px; overflow: hidden;
    background: var(--sheet);
    font-family: "Cabin", "Gill Sans", sans-serif;
    color: var(--ink);
  }
  .sheet { position: relative; width: 900px; height: 1200px; }

  .crop-marks { position: absolute; inset: 0; }

  .card {
    position: absolute; left: 66px; width: 768px; height: 438px;
    overflow: hidden;
  }
  .card--front { top: 60px; background: var(--white); }
  .card--back {
    top: 690px;
    background: linear-gradient(135deg, var(--olive-light), var(--olive) 55%, var(--olive-dark));
  }

  /* Front: brand panel */
  .brand-panel {
    position: absolute; left: 0; top: 0; width: 264px; height: 100%;
    background: linear-gradient(160deg, var(--olive-light), var(--olive) 60%, var(--olive-dark));
  }
  .brand-mark {
    position: absolute; left: 50%; top: 62px; width: 92px; height: 92px;
    margin-left: -46px; border-radius: 50%;
    background: var(--cream);
  }
  .brand-band {
    position: absolute; left: 0; top: 200px; width: 100%; height: 108px;
    background: var(--band);
    display: flex; flex-direction: column; align-items: center; justify-content: center;
    color: var(--cream);
  }
  .brand-band__name { font-size: 38px; font-weight: 400; letter-spacing: 1px; line-height: 1; }
  .brand-band__sub { margin-top: 10px; font-size: 12.5px; letter-spacing: 3px; text-transform: uppercase; }

  /* Front: contact details */
  .contact {
    position: absolute; right: 44px; top: 58px; text-align: right;
  }
  .contact__name { font-size: 36px; font-weight: 700; line-height: 1.05; }
  .contact__title { font-size: 21px; color: #4a4647; margin-top: 2px; }
  .contact__phones { margin-top: 36px; font-size: 23px; line-height: 1.25; }
  .contact__phones b { font-weight: 700; }
  .contact__email { margin-top: 26px; font-size: 21px; }
  .contact__web { margin-top: 20px; font-size: 22px; font-weight: 700; }

  /* Back */
  .back-mark {
    position: absolute; left: 0; right: 0; top: 120px; text-align: center;
    font-size: 64px; font-weight: 400; color: var(--white); letter-spacing: 2px;
  }
  .back-company {
    position: absolute; left: 0; right: 0; top: 326px; text-align: center;
    font-size: 25px; font-weight: 700; color: var(--white);
  }
  .back-address {
    position: absolute; left: 0; right: 0; top: 366px; text-align: center;
    font-size: 15.5px; color: var(--white);
  }
</style>
</head>
<body>
<main class="sheet">
  <svg class="crop-marks" width="900" height="1200" viewBox="0 0 900 1200" aria-hidden="true">
    <g stroke="var(--crop)" stroke-width="1.5">
      <line x1="66" y1="10" x2="66" y2="45"/>
      <line x1="834" y1="10" x2="834" y2="45"/>
      <line x1="10" y1="60" x2="50" y2="60"/>
      <line x1="850" y1="60" x2="890" y2="60"/>
      <line x1="10" y1="498" x2="50" y2="498"/>
      <line x1="850" y1="498" x2="890" y2="498"/>
      <line x1="66" y1="513" x2="66" y2="560"/>
      <line x1="834" y1="513" x2="834" y2="560"/>
      <line x1="66" y1="630" x2="66" y2="675"/>
      <line x1="834" y1="630" x2="834" y2="675"/>
      <line x1="10" y1="690" x2="50" y2="690"/>
      <line x1="850" y1="690" x2="890" y2="690"/>
      <line x1="10" y1="1128" x2="50" y2="1128"/>
      <line x1="850" y1="1128" x2="890" y2="1128"/>
      <line x1="66" y1="1143" x2="66" y2="1190"/>
      <line x1="834" y1="1143" x2="834" y2="1190"/>
    </g>
  </svg>

  <section class="card card--front">
    <div class="brand-panel">
      <div class="brand-mark"></div>
      <div class="brand-band">
        <span class="brand-band__name">Halvorne</span>
        <span class="brand-band__sub">Building &amp; Construction</span>
      </div>
    </div>
    <div class="contact">
      <p class="contact__name">Graham Whitley</p>
      <p class="contact__title">Chairman</p>
      <p class="contact__phones"><b>Phone</b> 512 555 0147<br><b>Mobile</b> 512 555 0148</p>
      <p class="contact__email">graham@halvornebuilding.com</p>
      <p class="contact__web">www.halvornebuilding.com</p>
    </div>
  </section>

  <section class="card card--back">
    <p class="back-mark">Halvorne</p>
    <p class="back-company">Halvorne Building &amp; Construction, Inc</p>
    <p class="back-address">2210 W. 41st St. &nbsp;|&nbsp; Austin, TX 78756 &nbsp;|&nbsp; Phone: (512) 555-0126 &nbsp;|&nbsp; Fax: (512) 555-0176</p>
  </section>
</main>
</body>
</html>
```